Luminously Grounded Vitality

We want to design a business card that is modern and appealing for an innovative psychedelic telemedicine company that provides at-home ketamine-assisted therapy along with wellness, longevity, and anti-aging medicines. We want to use our deep purple and white plus other colors you can find on our website. We don't have any strict brand guidelines yet so feel free to get creative. We want a very professional, but technology first modern design that will instill trust, peace, calm, but also be attractive to investors in the healthcare and SaaS space.

```html
<!DOCTYPE html>
<html lang="en">
<head>
<meta charset="utf-8">
<title>Luminously Grounded Vitality — Business Card</title>
<link href="https://fonts.googleapis.com/css2?family=Open+Sans:wght@400;700&display=swap" rel="stylesheet">
<style>
  :root {
    --bg: #dcdde0;
    --deep-purple: #7c66a8;
    --orchid: #b071a3;
    --orchid-dark: #a3639a;
    --brand-pink: #a65a93;
    --white: #ffffff;
    --shadow: rgba(40, 30, 60, 0.22);
  }
  * { margin: 0; padding: 0; box-sizing: border-box; }
  html, body { width: 1200px; height: 803px; overflow: hidden; }
  body {
    background: var(--bg);
    font-family: "Open Sans", sans-serif;
    position: relative;
  }
  .card {
    position: absolute;
    top: 260px;
    width: 500px;
    height: 284px;
    overflow: hidden;
    box-shadow: 0 14px 30px var(--shadow);
  }
  /* Front */
  .card-front { left: 50px; background: var(--white); }
  .front-band { position: absolute; inset: 0; width: 100%; height: 100%; }
  .holder {
    position: absolute; top: 22px; right: 26px; text-align: right; color: var(--white);
  }
  .holder-name { font-size: 19px; font-weight: 700; line-height: 1.2; }
  .holder-role { font-size: 15px; font-weight: 400; line-height: 1.3; }
  .contact {
    position: absolute; top: 128px; right: 26px; color: var(--white);
    font-size: 12.5px; line-height: 1.55; text-align: right;
  }
  .address { margin-bottom: 10px; }
  .contact-row { display: flex; justify-content: flex-end; align-items: center; gap: 10px; }
  .contact-icon {
    width: 15px; height: 15px; border-radius: 50%; background: var(--orchid);
    display: inline-flex; align-items: center; justify-content: center; flex: none;
  }
  .contact-icon svg { width: 9px; height: 9px; }
  .front-brand {
    position: absolute; left: 34px; bottom: 30px;
    display: flex; flex-direction: column; align-items: flex-start; gap: 10px;
  }
  .brand-dot { width: 14px; height: 14px; border-radius: 50%; background: var(--deep-purple); }
  .brand-name-front {
    color: var(--brand-pink); font-size: 18px; font-weight: 400; line-height: 1.25; letter-spacing: 0.2px;
  }
  /* Back */
  .card-back { left: 650px; background: var(--orchid); }
  .back-map {
    position: absolute; left: 40px; top: 30px; right: 40px; bottom: 30px;
    background: radial-gradient(ellipse at 55% 50%, var(--orchid-dark) 0%, rgba(163,99,154,0.5) 45%, rgba(176,113,163,0) 75%);
  }
  .back-brand {
    position: absolute; left: 0; right: 0; top: 104px;
    display: flex; justify-content: center; align-items: center; gap: 10px;
  }
  .brand-dot-back { width: 14px; height: 14px; border-radius: 50%; background: var(--white); }
  .brand-name-back { color: var(--white); font-size: 22px; font-weight: 400; }
  .back-web {
    position: absolute; left: 0; right: 0; top: 180px; text-align: center;
    color: var(--white); font-size: 14px; letter-spacing: 4px;
  }
</style>
</head>
<body>

  <section class="card card-front">
    <svg class="front-band" viewBox="0 0 500 284" preserveAspectRatio="none" aria-hidden="true">
      <polygon points="145,0 500,0 500,284 275,284" fill="var(--deep-purple)"/>
    </svg>

    <div class="holder">
      <p class="holder-name">Maren Ellison, FNP-C</p>
      <p class="holder-role">Co-founder</p>
    </div>

    <div class="contact">
      <p class="address">245 Alder Lane, Suite 300,<br>Boulder, CO, United States, Colorado</p>
      <p class="contact-row">+1 555-014-2290
        <span class="contact-icon"><svg viewBox="0 0 10 10"><path d="M2 1 L4 1 L4.5 3 L3.5 4 Q4.5 6 6 6.5 L7 5.5 L9 6 L9 8 Q5 9 2 5.5 Q1 3 2 1Z" fill="#fff"/></svg></span>
      </p>
      <p class="contact-row">hello@luminouslyvitality.com
        <span class="contact-icon"><svg viewBox="0 0 10 10"><rect x="1" y="2.5" width="8" height="5.5" fill="#fff"/><path d="M1 2.5 L5 5.5 L9 2.5" stroke="var(--orchid)" stroke-width="0.9" fill="none"/></svg></span>
      </p>
      <p class="contact-row">www.luminouslyvitality.com
        <span class="contact-icon"><svg viewBox="0 0 10 10"><circle cx="5" cy="5" r="3.8" stroke="#fff" stroke-width="0.9" fill="none"/><ellipse cx="5" cy="5" rx="1.6" ry="3.8" stroke="#fff" stroke-width="0.8" fill="none"/><line x1="1.2" y1="5" x2="8.8" y2="5" stroke="#fff" stroke-width="0.8"/></svg></span>
      </p>
    </div>

    <div class="front-brand">
      <span class="brand-dot"></span>
      <span class="brand-name-front">Luminously Grounded<br>Vitality</span>
    </div>
  </section>

  <section class="card card-back">
    <div class="back-map" role="img" aria-label="Faint dotted world map texture"></div>
    <div class="back-brand">
      <span class="brand-dot-back"></span>
      <span class="brand-name-back">Luminously Grounded Vitality</span>
    </div>
    <p class="back-web">www.luminouslyvitality.com</p>
  </section>

</body>
</html>
```